依頼概要
▽ターゲット
【■ 40~80歳■】向けの【■ ふとんの打ち直し■】販促用にポスターデザインを作成したいと考えており、デザイナー・クリエイターの方向けにコンペを開催いたします。

▽サイズ
【■A2サイズでトンボを付けて下さい。そのまま印刷屋に出せる形式(AIファイル必須■】

▽参考デザイン
サイト名:【■ ねむり堂川 ■】
参考URL:【■ http://www.nemuridokawa.co.jp/SHOP/582716/list.html■】

```html
<!DOCTYPE html>
<html lang="ja">
<head>
<meta charset="utf-8">
<title>おふとんの打直し ポスター</title>
<link rel="stylesheet" href="https://fonts.googleapis.com/css2?family=Noto+Sans+JP:wght@500;700;900&family=M+PLUS+Rounded+1c:wght@500;700;800&display=swap">
<style>
  :root{
    --stripe-a:#fbf1c4;
    --stripe-b:#fdf7dc;
    --ink:#1e1a16;
    --band:#ffffff;
    --lower-bg:#fbf4e2;
    --orange:#e8851d;
    --red:#e0341c;
    --box-bg:#fff3c2;
    --box-line:#f2c873;
    --frame:#c9c2b2;
    --sheep-tone:#efe7d6;
  }
  *{margin:0;padding:0;box-sizing:border-box}
  html,body{width:853px;height:1200px;overflow:hidden;background:#fff}
  .poster{
    position:relative;width:853px;height:1200px;overflow:hidden;
    border:2px solid var(--frame);
    background:repeating-linear-gradient(90deg,var(--stripe-a) 0 34px,var(--stripe-b) 34px 68px);
    font-family:"Noto Sans JP",sans-serif;color:var(--ink);
  }
  .headline{position:absolute;left:28px;top:48px;list-style:none}
  .headline li{
    display:inline-block;background:var(--band);
    font-weight:900;font-size:50px;line-height:1;letter-spacing:1px;
    padding:18px 26px 18px 24px;margin-bottom:22px;
  }
  .sheep{
    position:absolute;left:262px;top:400px;width:410px;height:240px;
    border-radius:48% 52% 45% 55%;
    background:radial-gradient(circle at 45% 45%,#fffdf6 0,var(--sheep-tone) 70%);
  }
  .lower{
    position:absolute;left:0;right:0;top:648px;bottom:0;background:var(--lower-bg);
  }
  .offer{
    position:absolute;left:32px;top:22px;
    font-family:"M PLUS Rounded 1c",sans-serif;font-weight:800;
    font-size:42px;color:var(--orange);letter-spacing:1px;
  }
  .prices{position:absolute;left:28px;right:28px;top:86px;display:flex;gap:22px}
  .price-card{
    flex:1;height:120px;border-radius:14px;background:var(--box-bg);
    border:2px solid var(--box-line);padding:12px 20px;
    font-family:"M PLUS Rounded 1c",sans-serif;
  }
  .price-card .size{display:block;font-weight:700;font-size:32px;color:var(--orange)}
  .price-card .amount{display:block;font-weight:800;font-size:40px;color:var(--red);margin-top:4px}
  .notes{position:absolute;left:32px;top:230px;list-style:none;font-size:24px;font-weight:500;line-height:42px}
  .notes li{display:flex;align-items:center;gap:6px}
  .notes svg{flex:none}
  .shop{
    position:absolute;left:0;right:0;bottom:34px;text-align:center;
    font-family:"M PLUS Rounded 1c",sans-serif;color:var(--orange);
  }
  .shop .tag{font-size:20px;font-weight:700;margin-right:14px}
  .shop .name{font-size:36px;font-weight:800}
</style>
</head>
<body>
<div class="poster">
  <ul class="headline">
    <li>毎晩、いい夢を見られたら、</li><br>
    <li>人生は2倍たのしめる。</li>
  </ul>

  <div class="sheep" role="img" aria-label="ぐっすり眠るふわふわの羊のイラスト"></div>

  <section class="lower">
    <h2 class="offer">おふとんの打直しでグッスリ快眠！</h2>

    <div class="prices">
      <div class="price-card"><span class="size">シングル</span><span class="amount">8,800円〜</span></div>
      <div class="price-card"><span class="size">セミダブル</span><span class="amount">9,800円〜</span></div>
      <div class="price-card"><span class="size">ダブル</span><span class="amount">10,800円〜</span></div>
    </div>

    <ul class="notes">
      <li><svg width="24" height="24" viewBox="0 0 24 24"><circle cx="12" cy="12" r="8" fill="none" stroke="var(--orange)" stroke-width="4"/></svg>ロング丈のお布団は上記価格＋1,000円でお仕立ていたします。</li>
      <li><svg width="24" height="24" viewBox="0 0 24 24"><circle cx="12" cy="12" r="8" fill="none" stroke="var(--orange)" stroke-width="4"/></svg>新品のお布団は上記価格＋3,000円でお仕立ていたします。</li>
      <li><svg width="24" height="24" viewBox="0 0 24 24"><circle cx="12" cy="12" r="8" fill="none" stroke="var(--orange)" stroke-width="4"/></svg>掛け布団の綿は保温性、吸湿性の優れた米綿をおすすめいたします。</li>
      <li><svg width="24" height="24" viewBox="0 0 24 24"><circle cx="12" cy="12" r="8" fill="none" stroke="var(--orange)" stroke-width="4"/></svg>お布団の柄は「男柄」、「女柄」をご選択いただけます。</li>
    </ul>

    <p class="shop"><span class="tag">クリーニングと寝具の店</span><span class="name">ふとんの北浦</span></p>
  </section>
</div>
</body>
</html>
```